Wolkenfeld - a property developer - Website design

Hi all!
Exciting new project for you! :)
We are looking for some creative/modern designs to best represent us as a company.
Please have a look at the following link: huhu.wolkenfeld.eu to get an idea about who we are and what we do.
The 'Main Page' of the HP should be neatly arranged, easy to navigate, contain several pictures (changing every 10 seconds or so) that should reflect that we are property developers.
The navigation points ('About us', 'Projects' 'Investment', 'Contact Us', 'Legal Notice') should be included in the Design (again under every navigation point, pictures may be added - that reflect our profession and/or the subsection)
What we will need at the end of the day is a fully functional site - i.e: a site that is designed and programmed with backend/wordpress, to allow us to make changes anytime we feel like it.
Further questions?! Don't hesitate to contact me! Thanks :)
Target Market(s)
Real Estate Development/Building sector
Industry/Entity Type
Real Estate Development
Number of Pages Required
5+ page
Look and feel

```html
<!DOCTYPE html>
<html lang="en">
<head>
<meta charset="utf-8">
<title>Wolkenfeld – Property Developer</title>
<link href="https://fonts.googleapis.com/css2?family=Open+Sans:wght@400;600;700&display=swap" rel="stylesheet">
<style>
:root{
  --yellow:#f7e400;
  --line-yellow:#f0df3a;
  --ink:#1d1d1d;
  --text:#555;
  --muted:#8a8a8a;
  --grey-word:#6e6e6e;
  --footer:#ececec;
  --btn:#111;
  --btn-text:#f3de2c;
}
*{box-sizing:border-box;margin:0;padding:0}
html,body{width:862px;height:1200px;overflow:hidden;background:#fff}
body{position:relative;font-family:"Open Sans",Arial,sans-serif;color:var(--text)}
.abs{position:absolute}
.top-rule{left:0;top:0;width:862px;height:2px;background:var(--yellow)}
.brand{display:flex;align-items:center;gap:6px;color:var(--ink);font-weight:600}
.brand-mark{width:20px;height:20px;background:var(--ink);flex:none}
.brand-name{display:block;font-size:21px;line-height:22px;letter-spacing:1px}
.brand-url{display:block;font-size:6px;line-height:8px;letter-spacing:.5px;font-weight:600}
.header-brand{left:70px;top:12px}
.footer-brand{left:520px;top:1051px}
.nav{left:0;top:24px;width:862px;height:20px;font-size:9.4px;color:#444}
.nav span{position:absolute;white-space:nowrap}
.nav .active::after{content:"";position:absolute;left:50%;top:14px;width:9px;height:5px;margin-left:-4px;background:#222;border:1px solid var(--yellow)}
.hero{left:0;top:58px;width:862px;height:318px;background:radial-gradient(ellipse at 70% 45%,#fbfbfb 0%,#ececec 60%,#dcdcdc 100%);border-bottom:2px solid var(--line-yellow)}
.hero-art{left:52px;top:22px;width:398px;height:296px;background:radial-gradient(ellipse at 50% 55%,#d9a86a 0%,#c9b59a 45%,rgba(230,230,230,0) 75%)}
.hero-copy{left:452px;top:142px;width:322px;text-align:center}
.hero-copy h1{font-size:16.8px;font-weight:700;color:var(--ink);letter-spacing:.2px}
.hero-copy h1 em,.section-title em{font-style:normal;color:var(--grey-word)}
.hero-copy p{font-size:9.1px;line-height:14.8px;color:#222;margin-top:4px}
.btn{display:inline-block;background:var(--btn);color:var(--btn-text);border-radius:3px;font-weight:600;white-space:nowrap}
.hero-copy .btn{font-size:9.5px;padding:6px 8px;margin-top:8px;border:1px solid #444}
.dots{left:414px;top:301px;display:flex;gap:7px}
.dots i{width:6px;height:6px;border-radius:50%;background:#b5b5b5}
.dots i.on{background:#d9c400}
.about{left:88px;top:398px;width:428px}
.section-title{font-size:11.6px;font-weight:700;color:var(--ink);letter-spacing:.2px}
.about p{font-size:8.8px;line-height:14.8px;margin-top:14px;text-align:justify}
.about p:first-of-type{margin-top:16px}
.btn.small{font-size:7px;padding:5px 6px}
.about .btn{margin-top:10px}
.about-photo{left:546px;top:402px;width:244px;height:172px;background:#fff;border:1px solid #ddd;padding:4px;box-shadow:0 6px 6px -4px #bbb}
.about-photo div{width:100%;height:100%;background:linear-gradient(180deg,#5a82d2 0%,#8fb0e6 28%,#f1f1f1 30%,#dcdcdc 80%,#8a6a4a 100%)}
.divider{left:0;width:862px;height:4px;border-top:1px solid #ddd;border-bottom:1px solid #ddd}
.divider-mark{width:12px;height:24px;background:#222;border:2px solid var(--yellow)}
.projects-title{left:0;top:666px;width:862px;text-align:center}
.band{left:0;top:748px;width:862px;height:136px;background:var(--yellow)}
.card{top:696px;width:157px}
.card-photo{height:93px;background:#fff;border:1px solid #ddd;padding:4px}
.card-photo div{width:100%;height:100%}
.card p{font-size:7.6px;line-height:15px;color:#222;margin-top:6px;text-align:justify;padding:0 2px}
.card b{font-weight:700}
.card .btn{margin:6px 0 0 2px}
.venture-title{left:0;top:919px;width:862px;text-align:center}
.partner{top:968px;font-size:10.5px;font-weight:600;color:#333;display:flex;align-items:center;gap:5px;white-space:nowrap}
.partner i{width:12px;height:12px;background:#d32}
.footer{left:0;top:1026px;width:862px;height:148px;background:var(--footer);border-top:2px solid var(--line-yellow)}
.col h3{font-size:11.5px;font-weight:600;color:#222}
.col{top:1045px;font-size:8.8px;color:#555}
.col ul{list-style:none;margin-top:5px}
.col li{line-height:14.7px}
.social li{display:flex;align-items:center;gap:8px;line-height:22.4px}
.social i{width:13px;height:13px;background:#fff;border:1px solid #d5d5d5}
.contact{font-size:8.8px;color:#222;line-height:15px}
.contact div{display:flex;align-items:center;gap:9px;white-space:nowrap}
.contact svg{width:9px;height:9px;fill:#333}
.bottom{left:0;top:1174px;width:862px;height:26px;text-align:center;font-size:7px;color:var(--muted);line-height:26px;border-bottom:2px solid var(--yellow)}
</style>
</head>
<body>
<div class="abs top-rule"></div>

<header>
  <div class="abs brand header-brand"><span class="brand-mark"></span><span><span class="brand-name">WOLKENFELD</span><span class="brand-url">WOLKENFELD.EU</span></span></div>
  <nav class="abs nav">
    <span class="active" style="left:434px">Home</span>
    <span style="left:480px">About us</span>
    <span style="left:538px">Projects</span>
    <span style="left:593px">Investment</span>
    <span style="left:661px">Contact us</span>
    <span style="left:726px">Legal Notice</span>
  </nav>
</header>

<section class="abs hero">
  <div class="abs hero-art" role="img" aria-label="Watercolour sketch of a modern living room interior with desk, chairs and plants"></div>
  <div class="abs hero-copy">
    <h1>WE ARE A PROPERTY <em>DEVELOPER</em></h1>
    <p>We place the highest value on location, architecture and features of our projects, and offer our clients to play an active role in the creation of their future residence.</p>
    <span class="btn">Read More</span>
  </div>
  <div class="abs dots"><i></i><i class="on"></i><i></i></div>
</section>

<section class="abs about">
  <h2 class="section-title">QUALITY, SKILLS AND EXPERIENCE: <em>EVERYTHING UNDER ONE ROOF.</em></h2>
  <p>Wolkenfeld is a combination of potent companies pursuing a common goal: the realization of modern, sustainable housing projects for highest demands in Vienna. Our building companies' efforts are concentrating on the two core areas of new developments and roof extensions.</p>
  <p>A high level of expertise, excellent quality and many years of experience provide a solid foundation for the realization of dream homes. Our Wolkenfeld companies combine the knowledge and know-how of more than 30 years under one roof.</p>
  <p>We want our customers to be satisfied for a long time – whether they want to invest in property or use an apartment themselves. Consulting on an equal basis is the main objective in our customer relations, from the first meeting, to the handover date.</p>
  <span class="btn small">Read More</span>
</section>
<div class="abs about-photo"><div role="img" aria-label="Photo of a white modern apartment building with terraces and planters under a blue sky"></div></div>

<div class="abs divider" style="top:632px"></div>
<div class="abs divider-mark" style="left:425px;top:622px"></div>

<h2 class="abs section-title projects-title">OUR <em>PROJECTS</em></h2>
<div class="abs band"></div>

<article class="abs card" style="left:93px">
  <div class="card-photo"><div role="img" aria-label="Photo of a small model house held in a hand" style="background:linear-gradient(135deg,#2f4a70,#6f8db0 55%,#c98a6a)"></div></div>
  <p><b>Lorem Ipsum</b> is simply dummy text of the printing and typesetting industry.</p>
  <span class="btn small">Read More</span>
</article>
<article class="abs card" style="left:266px">
  <div class="card-photo"><div role="img" aria-label="Photo of a city skyline with high-rise towers" style="background:linear-gradient(180deg,#8fb2d8,#c4d3e2 45%,#6b7680)"></div></div>
  <p><b>Lorem Ipsum</b> is simply dummy text of the printing and typesetting industry.</p>
  <span class="btn small">Read More</span>
</article>
<article class="abs card" style="left:439px">
  <div class="card-photo"><div role="img" aria-label="Photo of a large family house lit at dusk" style="background:linear-gradient(180deg,#7c9fd0,#b8b6ac 50%,#8a7a66)"></div></div>
  <p><b>Lorem Ipsum</b> is simply dummy text of the printing and typesetting industry.</p>
  <span class="btn small">Read More</span>
</article>
<article class="abs card" style="left:612px">
  <div class="card-photo"><div role="img" aria-label="Photo of a detached house surrounded by trees and garden" style="background:linear-gradient(180deg,#dfe8ef,#b9b39a 45%,#4f7a3a)"></div></div>
  <p><b>Lorem Ipsum</b> is simply dummy text of the printing and typesetting industry.</p>
  <span class="btn small">Read More</span>
</article>

<div class="abs divider-mark" style="left:425px;top:875px"></div>

<h2 class="abs section-title venture-title">WOLKENFELD IS A <em>JOINT VENTURE</em> BETWEEN</h2>
<div class="abs partner" style="left:290px"><i></i>Lindqvist Estates</div>
<div class="abs partner" style="left:412px">Morrow Holding</div>
<div class="abs partner" style="left:498px"><i style="background:#2a8fb0"></i>Calvaro Realty</div>

<footer class="abs footer"></footer>
<div class="abs col" style="left:72px">
  <h3>Quick Links</h3>
  <ul><li>Home</li><li>About us</li><li>Projects</li><li>Investment</li><li>Contact us</li><li>Legal Notice</li></ul>
</div>
<div class="abs col social" style="left:287px">
  <h3>Follow Us</h3>
  <ul><li><i></i>Friendwall</li><li><i></i>Chirpline</li><li><i></i>Circlenet</li></ul>
</div>
<div class="abs brand footer-brand"><span class="brand-mark"></span><span><span class="brand-name">WOLKENFELD</span><span class="brand-url">WOLKENFELD.EU</span></span></div>
<div class="abs contact" style="left:524px;top:1103px">
  <div><svg viewBox="0 0 10 10"><path d="M2 0h2l1 3-1.5 1a6 6 0 0 0 2.5 2.5L7 5l3 1v2c0 1-1 2-2 2C4 10 0 6 0 2 0 1 1 0 2 0z"/></svg>Phone: +43 1 555 0140</div>
  <div><svg viewBox="0 0 10 10"><rect x="2" y="0" width="6" height="3"/><rect x="0" y="3" width="10" height="7"/></svg>Fax: +43 1 555 0141</div>
  <div><svg viewBox="0 0 10 10"><path d="M0 2h10v1L5 6 0 3zM0 4l5 3 5-3v5H0z"/></svg>E-mail: info@wolkenfeld.at</div>
</div>
<div class="abs contact" style="left:657px;top:1103px">
  <div><svg viewBox="0 0 10 10"><path d="M5 0a3.5 3.5 0 0 1 3.5 3.5C8.5 6 5 10 5 10S1.5 6 1.5 3.5A3.5 3.5 0 0 1 5 0zm0 2a1.5 1.5 0 1 0 0 3 1.5 1.5 0 0 0 0-3z"/></svg>Ahornweg 12/TOP 4B</div>
  <div style="padding-left:15px">1230 Vienna - Austria</div>
</div>

<div class="abs bottom">© 2015 • www.companyname.com • PRIVACY POLICY</div>
</body>
</html>
```